A5 Certificate for a running Brisora Challenge

I would like a certificate designed called the "Brisora 50K Running Challenge"

It is presented to people that have run 50k in Mallorca across 10 runs. So they have to run 10 runs with a minimum distance of 5K per run. This gives a total of 50k.

The certificate will need:

1. Map of Mallorca in the background
2. Picture of a runner
3. Main title at the front to say "Brisora 50k Running Challenge"
4. Space to put the runners name on it. "Awarded to:"
5. Space to put the date the certificate is awarded. "Date Awarded:"

The design is then up to you but it needs to look official and professional. It is designed for teenagers so it needs to be "cool" and bold.

Any questions please ask.

Target Market(s)

Teenagers who want something cool and bold.

Font styles to use
Sans Serif

Colors
0556a4
fbee3f
33a6d7

Requirements
Must have
• 1. Map of Mallorca in the background
• 2. Picture of a runner
• 3. Main title at the front to say "Brisora 50k Running Challenge"
• 4. Space to put the runners name on it. "Awarded to:"
• 5. Space to put the date the certificate is awarded. "Date Awarded:"
Nice to have
• Mallorca is a sunny holiday location so it would be good to have sea blue colours and the sun in the design. to show the running challenge was done on a holiday island.

```html
<!DOCTYPE html>
<html lang="en">
<head>
<meta charset="utf-8">
<title>Brisora 50K Running Challenge – Certificate</title>
<link rel="stylesheet" href="https://fonts.googleapis.com/css2?family=Libre+Baskerville:wght@400;700&family=Dancing+Script:wght@600&display=swap">
<style>
  :root {
    --navy: #1b3a5e;
    --deep-blue: #0556a4;
    --dark-blue: #0d3f73;
    --sky-blue: #33a6d7;
    --sun-yellow: #fbee3f;
    --sun-orange: #f7b733;
    --map-yellow: #f8f0a0;
    --panel: #ffffff;
    --panel-edge: #e6ebf2;
    --frame-line: #8cc4e4;
    --ink: #1b3a5e;
    --seal-outer: #f7a93a;
    --seal-inner: #e38a3f;
  }
  * { margin: 0; padding: 0; box-sizing: border-box; }
  html, body { width: 1200px; height: 848px; overflow: hidden; background: #fff; }
  .certificate {
    position: relative;
    width: 1200px;
    height: 848px;
    overflow: hidden;
    font-family: "Libre Baskerville", Georgia, serif;
    color: var(--ink);
  }
  .sunburst {
    position: absolute; inset: 0;
    background: radial-gradient(circle at 50% 50%, var(--sun-yellow) 0%, #fbe04a 55%, var(--sun-orange) 100%);
  }
  .panel {
    position: absolute;
    left: 72px; top: 44px; width: 1092px; height: 760px;
    background: radial-gradient(ellipse at 50% 45%, var(--panel) 55%, var(--panel-edge) 100%);
    border: 2px solid var(--frame-line);
    box-shadow: 0 0 0 8px rgba(255,255,255,0.6);
  }
  .swooshes { position: absolute; inset: 0; }
  .island-map {
    position: absolute;
    left: 150px; top: 70px; width: 880px; height: 720px;
    background: var(--map-yellow);
    border-radius: 44% 52% 40% 48% / 38% 46% 54% 50%;
    opacity: 0.85;
  }
  .runner-photo {
    position: absolute;
    left: 532px; top: 90px; width: 128px; height: 168px;
    background: #fbf5c4;
    border: 2px solid #a9a9a9;
  }
  .title {
    position: absolute; left: 0; right: 0; top: 318px;
    text-align: center;
    font-size: 44px; font-weight: 700; letter-spacing: 0.5px;
    color: var(--navy);
  }
  .presented {
    position: absolute; left: 0; right: 0; top: 392px;
    text-align: center;
    font-size: 19px; color: var(--navy);
  }
  .name-line {
    position: absolute; left: 230px; width: 740px; top: 502px;
    border-top: 2px dashed #9aa6b4;
  }
  .achievement {
    position: absolute; left: 0; right: 0; top: 576px;
    text-align: center;
    font-size: 18px; color: var(--navy);
  }
  .sign-field {
    position: absolute; top: 680px; width: 176px;
    border-top: 1.5px solid var(--navy);
    text-align: center;
    font-family: "Dancing Script", cursive;
    font-size: 28px; color: var(--navy);
    padding-top: 2px;
  }
  .sign-field.date { left: 200px; }
  .sign-field.signature { left: 812px; }
  .seal {
    position: absolute; left: 540px; top: 644px; width: 112px; height: 112px;
  }
</style>
</head>
<body>
<main class="certificate">
  <div class="sunburst" role="img" aria-label="Yellow and orange sunburst rays radiating behind the certificate"></div>

  <svg class="swooshes" width="1200" height="848" viewBox="0 0 1200 848" aria-hidden="true">
    <path d="M0 0 H420 C300 20 150 90 0 250 Z" fill="var(--sky-blue)"/>
    <path d="M0 0 H330 C220 40 110 110 0 220 Z" fill="var(--deep-blue)"/>
    <path d="M0 0 H220 C140 40 60 90 0 150 Z" fill="var(--dark-blue)"/>
    <path d="M1200 520 C1180 660 1050 780 760 848 H1200 Z" fill="var(--sky-blue)"/>
    <path d="M1200 610 C1170 720 1040 800 860 848 H1200 Z" fill="var(--deep-blue)"/>
    <path d="M1200 700 C1160 780 1080 820 980 848 H1200 Z" fill="var(--dark-blue)"/>
  </svg>

  <section class="panel"></section>

  <div class="island-map" role="img" aria-label="Map of the island in the background"></div>

  <div class="runner-photo" role="img" aria-label="Photo of a runner"></div>

  <h1 class="title">BRISORA 50K RUNNING CHALLENGE</h1>
  <p class="presented">THIS CERTIFICATE IS PROUDLY PRESENTED TO</p>
  <div class="name-line"></div>
  <p class="achievement">Successfully finished the Brisora 50K Running Challenge.</p>

  <div class="sign-field date">Date Awarded</div>
  <div class="sign-field signature">Signature</div>

  <svg class="seal" viewBox="0 0 112 112" aria-hidden="true">
    <circle cx="56" cy="56" r="54" fill="var(--seal-outer)"/>
    <circle cx="56" cy="56" r="40" fill="#f9c46b"/>
    <circle cx="56" cy="56" r="30" fill="var(--seal-inner)"/>
  </svg>
</main>
</body>
</html>
```